Business card design for engineering firm specializing in defense industry.

We need a professional business card design. Something simple but stands out. We are an engineering company specializing in composites in the defense industry.
Industry/Entity Type
Defense
Contact Information for Business Card
A simple black business card with the Fibrolane yellow color is what we had in mind but open for other designs.
Colors
ffc214

```html
<!DOCTYPE html>
<html lang="en">
<head>
<meta charset="utf-8">
<title>Fibrolane Business Card</title>
<link href="https://fonts.googleapis.com/css2?family=Open+Sans:wght@400;600;700&display=swap" rel="stylesheet">
<style>
  :root {
    --brand-yellow: #ffc214;
    --card-black: #1c1d1f;
    --card-white: #ffffff;
    --ink: #1a1a1a;
    --ink-soft: #3a3a3a;
    --silver: #c9c9c9;
    --backdrop: #e9e7e4;
    --divider: #9a9a9a;
  }
  * { margin: 0; padding: 0; box-sizing: border-box; }
  html, body {
    width: 1200px; height: 864px; overflow: hidden;
    background: var(--backdrop);
    font-family: "Open Sans", Arial, sans-serif;
  }
  .sheet {
    width: 1200px; height: 864px;
    display: flex; align-items: center; justify-content: center; gap: 40px;
  }
  .card {
    width: 540px; height: 309px;
    position: relative;
    box-shadow: 0 6px 18px rgba(0,0,0,0.18);
  }
  /* Front */
  .card-front {
    background: var(--card-black);
    display: flex; flex-direction: column; align-items: center; justify-content: center;
  }
  .wordmark {
    display: flex; align-items: center; gap: 14px;
  }
  .wordmark-dot {
    width: 22px; height: 22px; background: var(--brand-yellow); border-radius: 50%;
  }
  .wordmark-name {
    font-weight: 700; font-size: 48px; letter-spacing: 0.5px; line-height: 1;
  }
  .card-front .wordmark-name { color: var(--silver); }
  .front-url {
    margin-top: 34px;
    color: var(--silver);
    font-size: 15px; letter-spacing: 7px;
  }
  /* Back */
  .card-back {
    background: var(--card-white);
    display: flex; align-items: center;
  }
  .back-logo {
    width: 270px; display: flex; justify-content: center;
  }
  .card-back .wordmark-name { color: var(--ink); font-size: 36px; }
  .card-back .wordmark-dot { width: 18px; height: 18px; }
  .back-divider {
    width: 1px; height: 200px; background: var(--divider);
  }
  .contact {
    padding-left: 26px; color: var(--ink-soft);
  }
  .contact-name { font-weight: 700; font-size: 20px; color: var(--ink); line-height: 1.1; }
  .contact-role { font-size: 14px; color: var(--brand-yellow); margin-bottom: 10px; }
  .contact-address { font-size: 13px; line-height: 1.35; margin-bottom: 2px; }
  .contact-list { list-style: none; font-size: 13px; line-height: 1.45; }
  .contact-list li { display: flex; align-items: center; gap: 8px; }
  .contact-list svg { width: 12px; height: 12px; fill: var(--ink); flex: none; }
</style>
</head>
<body>
<main class="sheet">
  <section class="card card-front">
    <div class="wordmark">
      <span class="wordmark-dot"></span>
      <span class="wordmark-name">Fibrolane</span>
    </div>
    <p class="front-url">www.fibrolane.com</p>
  </section>

  <section class="card card-back">
    <div class="back-logo">
      <div class="wordmark">
        <span class="wordmark-dot"></span>
        <span class="wordmark-name">Fibrolane</span>
      </div>
    </div>
    <div class="back-divider"></div>
    <div class="contact">
      <p class="contact-name">Daniel Hurst</p>
      <p class="contact-role">Founder</p>
      <p class="contact-address">2170 Harbor Ridge Road<br>Lakeview, NY 11552</p>
      <ul class="contact-list">
        <li><svg viewBox="0 0 12 12"><path d="M2 1h2.5l1 2.5-1.5 1a6 6 0 0 0 3.5 3.5l1-1.5 2.5 1V10a1 1 0 0 1-1 1A9 9 0 0 1 1 2a1 1 0 0 1 1-1z"/></svg>555 0142 7731</li>
        <li><svg viewBox="0 0 12 12"><path d="M3.5 0h5a1 1 0 0 1 1 1v10a1 1 0 0 1-1 1h-5a1 1 0 0 1-1-1V1a1 1 0 0 1 1-1zm0 1.5v8h5v-8z"/></svg>555 0187 2469</li>
        <li><svg viewBox="0 0 12 12"><path d="M3 0h6v3H3zM1 4h10v5H9v3H3V9H1zm3 4v3h4V8z"/></svg>555 0163 9104</li>
        <li><svg viewBox="0 0 12 12"><path d="M0 2h12v8H0zm1 1v.5l5 3.5 5-3.5V3z"/></svg>daniel@fibrolane.com</li>
        <li><svg viewBox="0 0 12 12"><circle cx="6" cy="6" r="6"/></svg>www.fibrolane.com</li>
      </ul>
    </div>
  </section>
</main>
</body>
</html>
```